Executive Summary - Soccer Facility

We need help creating an Executive Summary 4 page template (A3 size print measuring 29.7 x 42.0cm, 11.69 x 16.53 inches) for our indoor soccer facility business plan. Our colors are black and white with yellow accents. Can also use soccer turf green where needed.
A design we like can be found here - https://plavuo.com/brindlewickhouse/docs/kestrelmoor-exec-summary-designed_c517838225793d?e=0
We have the following sections;
Introduction, The Opportunity, The Facility, Projections, Who We Are, What We Need - How We'll Use It, Investor ROI.
We have some charts that need adding too of which we will work with the winning entry. This is when we will provide approved text to drop into the template.
Target Market(s)
30 - 40 year old professionals that play recreational soccer on weekends
Other font styles liked:
- Molot (logo text)
Look and feel

```html
<!DOCTYPE html>
<html lang="en">
<head>
<meta charset="utf-8">
<title>Kestrel Urban Soccer – Executive Summary</title>
<link href="https://fonts.googleapis.com/css2?family=Anton&family=Montserrat:wght@300;400;500;600&display=swap" rel="stylesheet">
<style>
:root{
  --yellow:#f5ec1f;
  --yellow-pale:#f8f39a;
  --black:#0d0d0d;
  --white:#ffffff;
  --grey:#555555;
  --turf:#4caf3c;
  --orange:#f06a22;
  --cyan:#2ec4e6;
  --blue:#7fb4e8;
  --pink:#ef7fb0;
  --lime:#a8d86a;
  --gold:#f2c31b;
}
*{margin:0;padding:0;box-sizing:border-box}
html,body{width:910px;height:1200px;overflow:hidden;background:var(--white)}
body{position:relative;font-family:'Montserrat',sans-serif;color:var(--black)}
.abs{position:absolute}
.spread{position:absolute;left:22px;width:806px;height:570px;background:var(--yellow);overflow:hidden}
.spread--front{top:16px}
.spread--inside{top:604px}
.hl{background:linear-gradient(transparent 50%,var(--yellow) 50%);padding:0 3px}
.hl-white{background:linear-gradient(transparent 50%,var(--white) 50%);padding:0 4px}
.heading{font-weight:400;text-transform:uppercase;letter-spacing:.5px;line-height:1;white-space:nowrap}
.ghost{position:absolute;font-family:'Montserrat',sans-serif;font-weight:300;line-height:1;color:rgba(255,255,255,.55)}
.placeholder{position:absolute}

/* ---------- front spread ---------- */
.front__strip{left:402px;top:0;width:404px;height:60px;background:var(--white)}
.front__edge{left:776px;top:0;width:30px;height:570px;background:var(--white)}
.front__panel{left:442px;top:0;width:334px;height:570px;background:var(--black)}
.front__band{left:402px;top:60px;width:404px;height:92px;background:var(--yellow)}
.front__url{left:442px;top:28px;width:334px;text-align:center;color:var(--white);font-size:12.5px;letter-spacing:.4px}
.title-box{left:420px;top:76px;width:372px;height:72px;border:2px solid var(--black);display:flex;align-items:center;justify-content:center}
.title-box h1{font-family:'Anton',sans-serif;font-weight:400;font-size:38px;letter-spacing:.3px;line-height:1;white-space:nowrap}
.tagline{left:464px;top:190px;color:var(--white);font-weight:300;font-size:29px;line-height:1.1;white-space:nowrap}
.brand-mark{left:664px;top:252px;width:110px;text-align:center;color:var(--white)}
.brand-mark__dot{width:30px;height:30px;border-radius:50%;background:var(--white);margin:0 auto 8px}
.brand-mark__name{font-family:'Anton',sans-serif;font-size:19px;letter-spacing:.5px}
.phone-photo{left:650px;top:340px;width:156px;height:230px;background:linear-gradient(160deg,#e9e9e9,#bdbdbd 55%,#d9c2a8)}
.intro-label{left:402px;top:396px;width:188px;height:32px;background:var(--yellow);display:flex;align-items:center;padding-left:54px;font-size:13px}
.intro-text{left:456px;top:446px;width:184px;color:var(--white);font-weight:300;font-size:7.8px;line-height:12.4px}

.plan-box{left:32px;top:32px;width:336px;height:510px;background:var(--white);border:2px solid var(--black)}
.sales-title{left:45px;top:46px;font-size:15px}
.sales-sub{left:46px;top:72px;width:150px;text-align:center;font-size:5.2px;line-height:7px}
.pie{left:112px;top:94px}
.legend{left:40px;top:100px;font-size:4.4px;line-height:11px}
.legend-keys{left:42px;top:193px;width:148px;display:grid;grid-template-columns:repeat(4,1fr);font-size:3.6px;row-gap:3px}
.legend-keys span{display:flex;align-items:center;gap:2px;white-space:nowrap}
.legend-keys i{display:inline-block;width:4px;height:4px;border-radius:50%}
.needs-title{left:212px;top:44px;height:262px;writing-mode:vertical-rl;font-size:10.5px;letter-spacing:.3px;background:linear-gradient(90deg,var(--yellow) 45%,transparent 45%);padding:2px 0}
.needs-text{left:234px;top:44px;width:124px;font-size:5.4px;line-height:8.2px}
.needs-text p{margin-bottom:7px}
.needs-text ul{list-style:none}
.needs-text li{padding-left:5px;position:relative}
.needs-text li::before{content:"•";position:absolute;left:0}
.proj-title{left:44px;top:222px;font-size:15px}
.proj-sub{font-size:7px;text-transform:uppercase}
.proj-physical{left:42px;top:250px}
.proj-list{left:42px;top:261px;width:160px;font-size:6.2px;line-height:8.2px;list-style:none}
.proj-list li{padding-left:6px;position:relative}
.proj-list li::before{content:"•";position:absolute;left:0}
.proj-financial{left:42px;top:322px}
.fin-table{left:42px;top:336px;width:182px;border-collapse:separate;border-spacing:1px;font-size:3.6px;color:var(--white)}
.fin-table td,.fin-table th{background:var(--black);font-weight:400;text-align:center;height:10px;padding:0 1px}
.fin-table th{font-size:5px;line-height:5px;height:14px}
.fin-table th small{display:block;font-size:3.2px}
.fin-table .hot{background:var(--yellow);color:var(--black)}
.fin-table td:first-child{text-align:left}
.roi-title{left:45px;top:400px;font-size:11.5px}
.roi-text{left:42px;top:424px;width:74px;font-size:6.3px;line-height:10px}
.who-panel{left:106px;top:392px;width:262px;height:150px;background:var(--black);clip-path:polygon(18% 0,100% 0,100% 100%,0 100%)}
.who-title{left:172px;top:399px;color:var(--white);font-size:11.5px}
.who-text{left:110px;top:414px;width:250px;height:126px;color:var(--white);font-weight:300;font-size:5.7px;line-height:8.8px;text-align:right}
.who-text__slope{float:left;width:48px;height:126px;shape-outside:polygon(0 0,48px 0,0 126px);shape-margin:4px}

/* ---------- inside spread ---------- */
.exec-box{left:16px;top:20px;width:454px;height:132px;background:var(--white)}
.exec-title{left:16px;top:26px;width:454px;text-align:center;font-size:18px}
.exec-col{top:56px;width:168px;font-size:7.6px;line-height:11.6px;font-weight:400}
.exec-col--a{left:26px}
.exec-col--b{left:208px}
.fact-box{left:234px;top:148px;width:236px;height:74px;background:var(--black);clip-path:polygon(8% 0,100% 0,100% 100%,0 100%)}
.fact-title{left:260px;top:156px;color:var(--white);font-size:14px}
.fact-text{left:252px;top:177px;width:210px;color:var(--white);font-weight:300;font-size:6px;line-height:8.6px;text-align:center}
.opp-title{left:20px;top:184px;height:178px;writing-mode:vertical-rl;transform:rotate(180deg);font-size:16px;text-align:center;background:linear-gradient(90deg,var(--white) 38%,transparent 38%);padding:0 1px}
.opp-text{left:48px;top:172px;width:158px;font-size:7.6px;line-height:12px}
.opp-text p+p{margin-top:10px}
.video-caption{left:6px;top:392px;font-size:7.2px}
.video-still{left:6px;top:406px;width:180px;height:142px;background:linear-gradient(180deg,#b8bcc4 0 6%,#1e2a3a 6%,#2e4a2a 70%,#9aa0a8 70% 78%,#d6d6d6 78%)}
.diff-text{left:212px;top:228px;width:256px;font-size:8.6px;line-height:11.5px}
.compare{left:212px;top:292px;width:252px;border-collapse:collapse;table-layout:fixed}
.compare th{background:var(--black);color:var(--white);font-weight:400;font-size:7.6px;line-height:8px;height:26px;border:1px solid var(--yellow)}
.compare td{background:var(--white);height:28px;border:1px solid var(--yellow);font-size:5.6px;line-height:7px;color:var(--grey);padding:0 6px;text-align:center}
.compare td:first-child{text-align:left}
.mark{display:inline-block;width:11px;height:11px;vertical-align:middle}
.niche-box{left:194px;top:500px;width:318px;height:70px;background:var(--white);display:grid;grid-template-columns:1fr 1fr;gap:10px;padding:9px 10px 0 14px;font-size:5.3px;line-height:10.4px;color:var(--grey)}
.fac-title{left:446px;top:14px;font-size:25px}
.fac-frame{left:490px;top:56px;width:282px;height:188px;border-top:1.5px solid var(--black);border-right:1.5px solid var(--black)}
.fac-photo{left:500px;top:66px;width:262px;height:166px;background:linear-gradient(180deg,#a8b4bf 0 18%,#6e7f86 18% 40%,#8c8e86 40%,#5e625b)}
.fac-feats{left:482px;top:240px;width:256px;display:grid;grid-template-columns:128px 128px;row-gap:7px;font-size:6.4px;line-height:8px}
.fac-feats li{list-style:none;display:flex;align-items:center;gap:6px}
.fac-feats svg{flex:none}
.soon{left:748px;top:238px;width:40px;height:116px;background:var(--white);display:flex;align-items:center;justify-content:center}
.soon span{writing-mode:vertical-rl;font-size:16px;line-height:17px;letter-spacing:.5px;white-space:nowrap}
.bm-title{left:476px;top:322px;font-size:23px}
.core{left:480px;top:360px;display:flex;align-items:center;gap:5px;font-size:12px}
.pct{background:var(--black);color:var(--white);font-size:17px;font-weight:500;padding:1px 3px;line-height:19px}
.rev-list{font-size:8.2px;line-height:12px;list-style:none;white-space:nowrap}
.rev-list li{padding-left:8px;position:relative}
.rev-list li::before{content:"•";position:absolute;left:0}
.rev-list--core{left:486px;top:386px}
.ancillary{left:476px;top:462px;display:flex;align-items:center;gap:7px;font-size:12px}
.rev-list--anc{left:530px;top:490px}
.perks-box{left:686px;top:368px;width:120px;height:202px;background:var(--white)}
.perks{left:692px;top:374px;width:112px;list-style:none;font-size:5.8px;line-height:8.4px}
.perks li{display:flex;gap:3px}
.perks b{flex:none;width:7px;height:7px;border-radius:50%;background:var(--black);color:var(--white);font-size:4.6px;line-height:7px;text-align:center;font-weight:500;margin-top:1px}
.match-photo{left:692px;top:440px;width:112px;height:124px;background:linear-gradient(180deg,#d9dce2 0 30%,#6a7a8c 30% 40%,#3f6e3a 40%,#2f5a2c)}
</style>
</head>
<body>

<!-- Front spread: cover + plan overview -->
<section class="spread spread--front">
  <div class="abs front__strip"></div>
  <div class="abs front__edge"></div>
  <div class="abs front__panel"></div>
  <div class="abs front__band"></div>
  <p class="abs front__url">www.kestrelurbansoccer.com</p>
  <div class="abs title-box"><h1>KESTREL URBAN SOCCER</h1></div>
  <p class="abs tagline">“Experience<br>The Future<br>Of Indoor<br>Soccer. ”</p>
  <div class="abs brand-mark"><div class="brand-mark__dot"></div><div class="brand-mark__name">KESTREL</div></div>
  <div class="placeholder phone-photo" role="img" aria-label="Photo of a hand holding a smartphone showing the club app icon"></div>
  <div class="abs intro-label">INTRODUCTION</div>
  <p class="abs intro-text">Indoor soccer in the U.S. is a near $1bn industry with no market leader and no clear identity on the broader sporting landscape. This lack of identity has led to a cookie cutter approach to facilities nationwide and a distinct lack of atmosphere at venues. Kestrel Urban Soccer is here to redefine the market.</p>

  <div class="ghost" style="left:2px;top:514px;font-size:58px;color:var(--yellow-pale)">ROI</div>
  <div class="abs plan-box"></div>

  <h2 class="abs heading sales-title"><span class="hl">Sales Forecast</span></h2>
  <p class="abs sales-sub">3 YEARS CUMULATIVE SALES<br>THE IMPORTANCE OF DIVERSIFYING INCOME</p>
  <ul class="abs legend" style="list-style:none">
    <li style="color:var(--lime)">Advertising: 109,000 $</li>
    <li style="color:var(--pink)">Merchandise: 34,000 $</li>
    <li style="color:var(--orange)">Concessions: 30,000 $</li>
    <li style="color:var(--cyan)">Private Rentals: 26,000 $</li>
    <li style="color:var(--blue)">Youth Programs: 145,000 $</li>
    <li style="color:var(--gold)">Tournaments: 70,000 $</li>
    <li style="color:#e04b2a">Memberships: 207,360 $</li>
  </ul>
  <svg class="abs pie" width="90" height="90" viewBox="0 0 90 90">
    <g transform="rotate(-90 45 45)" fill="none" stroke-width="44">
      <circle cx="45" cy="45" r="22" pathLength="100" stroke="var(--turf)" stroke-dasharray="50 100"/>
      <circle cx="45" cy="45" r="22" pathLength="100" stroke="var(--orange)" stroke-dasharray="14 100" stroke-dashoffset="-50"/>
      <circle cx="45" cy="45" r="22" pathLength="100" stroke="var(--gold)" stroke-dasharray="8 100" stroke-dashoffset="-64"/>
      <circle cx="45" cy="45" r="22" pathLength="100" stroke="var(--cyan)" stroke-dasharray="10 100" stroke-dashoffset="-72"/>
      <circle cx="45" cy="45" r="22" pathLength="100" stroke="var(--blue)" stroke-dasharray="6 100" stroke-dashoffset="-82"/>
      <circle cx="45" cy="45" r="22" pathLength="100" stroke="var(--pink)" stroke-dasharray="5 100" stroke-dashoffset="-88"/>
      <circle cx="45" cy="45" r="22" pathLength="100" stroke="var(--lime)" stroke-dasharray="7 100" stroke-dashoffset="-93"/>
    </g>
  </svg>
  <div class="abs legend-keys">
    <span><i style="background:var(--turf)"></i>Registration</span>
    <span><i style="background:var(--orange)"></i>Memberships</span>
    <span><i style="background:var(--gold)"></i>Tournaments</span>
    <span><i style="background:var(--cyan)"></i>Youth Programs</span>
    <span><i style="background:var(--blue)"></i>Private Rentals</span>
    <span><i style="background:var(--pink)"></i>Concessions</span>
    <span><i style="background:var(--lime)"></i>Merchandise</span>
    <span><i style="background:#e04b2a"></i>Advertising</span>
  </div>

  <h2 class="abs heading needs-title">What We Need - How We'll Use It</h2>
  <div class="abs needs-text">
    <p>Kestrel Urban Soccer is currently seeking seed funding of $250,000 - $350,000 for stage 1 (launch phase) of their proposed National City facility.</p>
    <p>These funds will be spent on start-up expenses associated with site development including permitting, consultancy fees, building design and renovation, playing surface installation, off-field and online infrastructure, marketing and customer acquisition.</p>
    <p>The seed capital will be used over the first year of operations to reach the following business goals:</p>
    <ul>
      <li>Develop National City site and launch competitions</li>
      <li>Grow team patronage to 60% capacity</li>
      <li>Continue rolling out new features to build out from minimum viable product</li>
      <li>Build a unique brand and loyal following through key milestones and metrics</li>
      <li>Diversify income streams and increase ancillary income to 20%</li>
      <li>Test, tweak, and launch beta version of Kestrel App</li>
      <li>Finalize a feasibility study into site purchase, a second field, and Series A funding found</li>
    </ul>
  </div>

  <h2 class="abs heading proj-title"><span class="hl">Projections</span></h2>
  <h3 class="abs proj-sub proj-physical" style="font-weight:400">Physical</h3>
  <ul class="abs proj-list">
    <li>Approximately 600,000 impressions (via on-site billboard) to I-5 north bound visitors weekly</li>
    <li>124 teams &amp; 1000+ players</li>
    <li>75,000 visitors per year and over</li>
  </ul>
  <h3 class="abs proj-sub proj-financial" style="font-weight:400">Financial</h3>
  <table class="abs fin-table">
    <tr><th></th><th>2017<small>(6Qx)</small></th><th>2018<small>(7Qx)</small></th><th class="hot">2019<small>(9Qx)</small></th><th>2019<small>(2 fields)</small></th><th>2020<small>(15Qx)</small></th><th>2021<small>(20Qx)</small></th></tr>
    <tr><td>Revenue</td><td>$481,846</td><td>$571,520</td><td class="hot">$680,184</td><td>$1,182,910</td><td>$1,725,302</td><td>$1,769,260</td></tr>
    <tr><td>Expenses</td><td>$390,066</td><td>$378,775</td><td class="hot">$387,351</td><td>$618,574</td><td>$1,396,204</td><td>$1,405,262</td></tr>
    <tr><td>Net Profit</td><td>$91,780</td><td>$192,745</td><td class="hot">$295,833</td><td>$494,416</td><td>$329,098</td><td>$363,998</td></tr>
  </table>

  <h2 class="abs heading roi-title"><span class="hl">Investor ROI</span></h2>
  <p class="abs roi-text">Quarterly investor updates and dividends will be distributed and paid to all investors with the annual return forecast between $1,500 - $3,500.</p>

  <div class="abs who-panel"></div>
  <div class="ghost" style="left:346px;top:402px;font-size:58px">W</div>
  <h2 class="abs heading who-title">Who Are We?</h2>
  <div class="abs who-text"><div class="who-text__slope"></div>The strengths of Kestrel Urban Soccer are intrinsically linked with the skills and experiences of its two founders. Having both played numerous forms of indoor soccer across different continents, running federation affiliated clubs and tournaments and participating in international soccer tournaments, Owen Tallis and Mateo Arvane have spent the past year researching and predicting the future trends of the indoor market. Together with over 30 years combined experience in fundraising, sales, civic engagement and event management from Federal Government through top-500 companies, their partnership and innovative approach to the recreational side of the game are a strong value proposition for future investors.</div>
</section>

<!-- Inside spread: summary, opportunity, facility, business model -->
<section class="spread spread--inside">
  <div class="ghost" style="left:698px;top:-6px;font-size:84px">TF</div>
  <div class="ghost" style="left:382px;top:58px;font-size:80px">ES</div>
  <div class="ghost" style="left:2px;top:522px;font-size:52px">Fo</div>

  <div class="abs exec-box"></div>
  <h2 class="abs heading exec-title"><span class="hl">Executive Summary</span></h2>
  <p class="abs exec-col exec-col--a">Kestrel Urban Soccer is a California Corporation that owns and operates boutique indoor soccer facilities focused on quality across all facets of the player experience, innovative soccer technology and being a unique social hub of the communities of which they service.</p>
  <p class="abs exec-col exec-col--b">Our vision is to be the leading indoor soccer facility chain across the country. We aim to achieve this through our innovative approaches to the game and building a loyal and interconnected player network, culminating in a respected lifestyle brand.</p>

  <div class="abs fact-box"></div>
  <h2 class="abs heading fact-title">Did You Know?</h2>
  <p class="abs fact-text">The current indoor format was created due to North Americans' familiarity with hockey and the existence of hockey arenas, which then adapted their game for these facilities.</p>

  <h2 class="abs heading opp-title">The Opportunity</h2>
  <div class="abs opp-text">
    <p>Kestrel Urban Soccer is as much a lifestyle brand as it is an indoor soccer facility. It understands and engages its patrons rather than perform the basic duties of a transactional entity that refuses to be flexible in a changing economy.</p>
    <p>Our research has shown that the market is ripe for a new type of indoor soccer facility, one that provides more personalization, connectivity and value to players and transforms venues into unique soccer hubs that players, supporters, friends, and families</p>
  </div>
  <p class="abs video-caption">Example of weekly video highlights:</p>
  <div class="placeholder video-still" role="img" aria-label="Desktop monitor showing a weekly indoor match highlight video"></div>

  <p class="abs diff-text">Kestrel Urban Soccer's focus on combining an enhanced player experience with personalized technology (including an app, in-game video and packaged highlights) is a key differentiator in this market and will drive future growth.</p>

  <table class="abs compare">
    <colgroup><col style="width:104px"><col style="width:74px"><col style="width:74px"></colgroup>
    <tr><th>Services</th><th>Current Indoor Soccer</th><th>Kestrel Urban Soccer</th></tr>
    <tr><td>Organized leagues</td><td><svg class="mark" viewBox="0 0 12 12"><circle cx="6" cy="6" r="6" fill="#0d0d0d"/><path d="M4 4l4 4M8 4l-4 4" stroke="#fff" stroke-width="1.3"/></svg></td><td><svg class="mark" viewBox="0 0 12 12"><circle cx="6" cy="6" r="6" fill="#0d0d0d"/><path d="M4 4l4 4M8 4l-4 4" stroke="#fff" stroke-width="1.3"/></svg></td></tr>
    <tr><td>App to connect with team and see latest live stats</td><td></td><td><svg class="mark" viewBox="0 0 12 12"><circle cx="6" cy="6" r="6" fill="#0d0d0d"/><path d="M4 4l4 4M8 4l-4 4" stroke="#fff" stroke-width="1.3"/></svg></td></tr>
    <tr><td>Team personalization - logos &amp; kits</td><td></td><td><svg class="mark" viewBox="0 0 12 12"><circle cx="6" cy="6" r="6" fill="#0d0d0d"/><path d="M4 4l4 4M8 4l-4 4" stroke="#fff" stroke-width="1.3"/></svg></td></tr>
    <tr><td>Video highlight packages</td><td></td><td><svg class="mark" viewBox="0 0 12 12"><circle cx="6" cy="6" r="6" fill="#0d0d0d"/><path d="M4 4l4 4M8 4l-4 4" stroke="#fff" stroke-width="1.3"/></svg></td></tr>
    <tr><td>Community engagement</td><td></td><td><svg class="mark" viewBox="0 0 12 12"><circle cx="6" cy="6" r="6" fill="#0d0d0d"/><path d="M4 4l4 4M8 4l-4 4" stroke="#fff" stroke-width="1.3"/></svg></td></tr>
    <tr><td>Weekend Finals &amp; Tournaments</td><td></td><td><svg class="mark" viewBox="0 0 12 12"><circle cx="6" cy="6" r="6" fill="#0d0d0d"/><path d="M4 4l4 4M8 4l-4 4" stroke="#fff" stroke-width="1.3"/></svg></td></tr>
  </table>

  <div class="abs niche-box">
    <p>Flexibility and innovation is a necessity for success and carving out a niche in the market. Many indoor soccer venues are limited with their services due to the necessity of maximizing league participation in the evenings and leaving</p>
    <p>little time to appeal to larger (and more lucrative) junior markets. The fields are also often oversized and cannot serve multiple functions because they are contained within rigid, purpose-built walls.</p>
  </div>

  <h2 class="abs heading fac-title"><span class="hl-white">The Facility</span></h2>
  <div class="abs fac-frame"></div>
  <div class="placeholder fac-photo" role="img" aria-label="Aerial map view of the downtown waterfront with the facility site pinned"></div>
  <ul class="abs fac-feats">
    <li><svg width="16" height="16" viewBox="0 0 18 18"><circle cx="9" cy="9" r="9" fill="#0d0d0d"/><circle cx="9" cy="9" r="5" fill="none" stroke="#fff" stroke-width="1.2"/><path d="M9 6v3h2.5" stroke="#fff" stroke-width="1.2" fill="none"/></svg>5 minutes from down- town San Diego</li>
    <li><svg width="16" height="16" viewBox="0 0 18 18"><circle cx="9" cy="9" r="9" fill="#0d0d0d"/><rect x="5.5" y="5" width="7" height="8" fill="none" stroke="#fff" stroke-width="1.1"/><path d="M5.5 9h7M9 5v8" stroke="#fff" stroke-width="1"/></svg>2 story building with urban theme</li>
    <li><svg width="16" height="16" viewBox="0 0 18 18"><circle cx="9" cy="9" r="9" fill="#0d0d0d"/><rect x="5" y="5" width="8" height="8" fill="none" stroke="#fff" stroke-width="1.2"/></svg>15,670 sq. ft.</li>
    <li><svg width="16" height="16" viewBox="0 0 18 18"><circle cx="9" cy="9" r="9" fill="#0d0d0d"/><rect x="4.5" y="6" width="9" height="6" rx="1" fill="none" stroke="#fff" stroke-width="1.1"/></svg>Electronic advertising hoarding</li>
    <li><svg width="16" height="16" viewBox="0 0 18 18"><circle cx="9" cy="9" r="9" fill="#0d0d0d"/><circle cx="9" cy="5.5" r="1.1" fill="#fff"/><path d="M9 8v5" stroke="#fff" stroke-width="1.6"/></svg>Field is within regulation futsal dimension</li>
    <li><svg width="16" height="16" viewBox="0 0 18 18"><circle cx="9" cy="9" r="9" fill="#0d0d0d"/><path d="M7 5.5l5 3.5-5 3.5z" fill="#fff"/></svg>Full video &amp; sound</li>
  </ul>
  <div class="abs soon"><span>COMING<br>SOON...</span></div>

  <h2 class="abs heading bm-title"><span class="hl-white">Business Model</span></h2>
  <div class="abs core"><span>CORE REVENUE</span><span class="pct">80%</span></div>
  <ul class="abs rev-list rev-list--core">
    <li>Competitive Soccer Leagues</li>
    <li>Youth Instructional programs</li>
    <li>Tournaments</li>
    <li>School programs</li>
    <li>Private Rentals</li>
    <li>Sponsorship &amp; advertising</li>
  </ul>
  <div class="abs ancillary"><span class="pct">20%</span><span>ANCILLARY REVENUE</span></div>
  <ul class="abs rev-list rev-list--anc">
    <li>Retail &amp; equipment sales</li>
    <li>Memberships</li>
    <li>Niche partnerships</li>
    <li>Concessions</li>
    <li>Games zone/Classroom</li>
    <li>Community Events</li>
  </ul>

  <div class="abs perks-box"></div>
  <ul class="abs perks">
    <li><b>1</b>Weekly highlight videos</li>
    <li><b>2</b>Interactive Kestrel App</li>
    <li><b>3</b>Viewing deck</li>
    <li><b>4</b>Free personalized kits for each team</li>
    <li><b>5</b>Junior clinics</li>
  </ul>
  <div class="placeholder match-photo" role="img" aria-label="Players during an indoor soccer match on green turf with branded boards"></div>
</section>

</body>
</html>
```